Design an Outstanding flyer for my company.

I need a flyer designed for our window tinting company based in Brisbane Queensland Australia. The flyer will be targeting Home tinting. We also do mobile car tinting. Something in regards to this could be incorporated into the flyer as well.
I want it to be 2 sided DL size. Black background.
It really needs to Pop, and be a real attention getter.
It needs to be easy to read.
I have provided a mock up with the info on it from our marketing company. It will need a spellcheck etc to make sure everything is correct.
Everything about it can be changed however you like.
I have also included the company logo.

Lets see what you've got!

Target Market(s)

Home Owners

Industry/Entity Type

Home Improvement

Other font styles liked:
• Duan Penh

Requirements
Must have
• All the information on the mock up. Clear and easy to read.
• Must Stand Out!

```html
<!DOCTYPE html>
<html lang="en">
<head>
<meta charset="utf-8">
<title>Brightway Tinting – Home Window Tinting Flyer</title>
<link href="https://fonts.googleapis.com/css2?family=Arimo:wght@700&family=Roboto+Condensed:wght@400;700&family=Open+Sans:wght@400&display=swap" rel="stylesheet">
<style>
  :root {
    --page: #ffffff;
    --ink: #0b0b0b;
    --facet-dark: #1c1c1c;
    --facet-mid: #3a3a3a;
    --facet-light: #6e6e6e;
    --yellow: #f7ec1c;
    --gold: #fbc70b;
    --white: #ffffff;
    --url-ink: #1a1a1a;
  }
  * { margin: 0; padding: 0; box-sizing: border-box; }
  html, body { width: 996px; height: 1200px; overflow: hidden; background: var(--page); }
  .canvas { position: relative; width: 996px; height: 1200px; }
  .flyer-shadow {
    position: absolute; left: 230px; top: 1040px; width: 560px; height: 30px;
    border-radius: 50%; background: rgba(0,0,0,0.18); filter: blur(12px);
  }
  .flyer {
    position: absolute; left: 255px; top: 78px; width: 504px; height: 974px;
    background: var(--ink); overflow: hidden; text-align: center;
  }
  .flyer-art { position: absolute; inset: 0; }
  .headline {
    position: absolute; left: 0; width: 100%;
    font-family: "Arimo", Arial, sans-serif; font-weight: 700; line-height: 1;
    white-space: nowrap;
  }
  .headline--white { color: var(--white); }
  .headline--yellow { color: var(--yellow); }
  .h-heat { top: 62px; font-size: 53px; }
  .h-uv { top: 118px; font-size: 37px; }
  .h-money { top: 163px; font-size: 67px; }
  .h-privacy { top: 236px; font-size: 43px; }
  .benefits {
    position: absolute; left: 46px; width: 412px; top: 302px;
    font-family: "Roboto Condensed", "Arial Narrow", sans-serif; font-weight: 400;
    font-size: 13.4px; line-height: 19.7px; color: var(--white); text-transform: uppercase;
  }
  .reasons {
    position: absolute; top: 478px; left: 0; width: 100%;
    font-family: "Roboto Condensed", "Arial Narrow", sans-serif; font-weight: 400;
    font-size: 30px; line-height: 35px; color: var(--yellow);
  }
  .divider { position: absolute; left: 128px; width: 248px; height: 3px; background: var(--gold); }
  .divider--one { top: 594px; }
  .divider--two { top: 692px; }
  .call {
    position: absolute; top: 605px; left: 0; width: 100%;
    font-family: "Roboto Condensed", "Arial Narrow", sans-serif; font-weight: 700;
    font-size: 31px; line-height: 40px; color: var(--white);
  }
  .contact {
    position: absolute; top: 705px; left: 0; width: 100%;
    font-family: "Roboto Condensed", "Arial Narrow", sans-serif; font-weight: 700;
    font-size: 35px; line-height: 42px; color: var(--yellow);
  }
  .brand {
    position: absolute; top: 812px; left: 0; width: 100%;
    display: flex; align-items: center; justify-content: center; gap: 16px;
  }
  .brand-dot { width: 46px; height: 46px; border-radius: 50%; background: var(--gold); }
  .brand-name {
    font-family: "Roboto Condensed", "Arial Narrow", sans-serif; font-weight: 700;
    font-size: 44px; color: var(--gold); letter-spacing: 1px;
  }
  .website {
    position: absolute; top: 938px; left: 178px;
    font-family: "Open Sans", Arial, sans-serif; font-size: 17px; color: var(--url-ink);
  }
</style>
</head>
<body>
<div class="canvas">
  <div class="flyer-shadow"></div>
  <section class="flyer">
    <svg class="flyer-art" width="504" height="974" viewBox="0 0 504 974" aria-hidden="true">
      <defs>
        <linearGradient id="facetA" x1="0" y1="0" x2="1" y2="1">
          <stop offset="0" stop-color="#8a8a8a"/><stop offset="0.35" stop-color="#2e2e2e"/><stop offset="1" stop-color="#101010"/>
        </linearGradient>
        <linearGradient id="facetB" x1="1" y1="0" x2="0" y2="1">
          <stop offset="0" stop-color="#4a4a4a"/><stop offset="1" stop-color="#0d0d0d"/>
        </linearGradient>
        <linearGradient id="goldBand" x1="0" y1="0" x2="1" y2="0">
          <stop offset="0" stop-color="#f7ec1c"/><stop offset="1" stop-color="#fbc70b"/>
        </linearGradient>
      </defs>
      <polygon points="0,0 504,45 504,974 0,974" fill="#121212"/>
      <polygon points="0,8 504,50 504,120 0,110" fill="url(#facetA)"/>
      <polygon points="0,0 30,0 504,640 504,700 0,60" fill="url(#facetB)"/>
      <polygon points="0,540 504,720 504,974 0,974" fill="#1a1a1a"/>
      <polygon points="0,530 240,620 460,974 0,974" fill="url(#facetB)" opacity="0.7"/>
      <polygon points="504,420 504,974 340,974" fill="#2a2a2a"/>
      <polygon points="200,0 504,420 504,560" fill="#3a3a3a" opacity="0.5"/>
      <polygon points="30,0 504,0 504,48" fill="url(#goldBand)"/>
      <polygon points="0,0 30,0 504,48 504,56 0,12" fill="#cfcfcf" opacity="0.7"/>
      <polygon points="504,637 504,742 450,742" fill="url(#goldBand)"/>
      <polygon points="120,930 504,930 504,974 80,974" fill="url(#goldBand)"/>
    </svg>

    <div class="headline headline--white h-heat">KEEP HEAT OUT</div>
    <div class="headline headline--yellow h-uv">BLOCK 99.9% UV RAYS</div>
    <div class="headline headline--white h-money">SAVE MONEY</div>
    <div class="headline headline--yellow h-privacy">INCREASE PRIVACY</div>

    <p class="benefits">Reduce glare. Reduce energy costs. Control the amount of light entering your home. Reduce carbon footprint. Make home more beautiful. Eliminate home hot spots. Protect against broken glass. Regulate energy. Protects upholstery. Improve effectiveness of roof insulation. Improve health. Reduces interior floor fading. Eliminate need for blinds. Strengthen your windows. Insulate in winter. Affordable.</p>

    <p class="reasons">20 REASONS WHY<br>HOME WINDOW TINTING<br>IS PERFECT FOR YOU.</p>
    <div class="divider divider--one"></div>
    <p class="call">CALL BRISBANE’S LEADER IN<br>HOME WINDOW TINTING NOW.</p>
    <div class="divider divider--two"></div>
    <p class="contact">TEL 07 3000 5821<br>SMS: 0400 555 018</p>

    <div class="brand">
      <span class="brand-dot"></span>
      <span class="brand-name">BRIGHTWAY TINTING</span>
    </div>

    <p class="website">www.brightwaytinting.com.au</p>
  </section>
</div>
</body>
</html>
```